Harbinger Slabworks, Inc. Business Card

Create a business card that is eye catching and based around concrete sawcutting. I've attached our current business card and logo for reference. We like aspects of the current business card, but it is starting to feel very loud and lost. We would like something that is still fun but is more modern and streamlined.

```html
<!DOCTYPE html>
<html lang="en">
<head>
<meta charset="utf-8">
<title>Harbinger Slabworks, Inc. Business Card</title>
<link href="https://fonts.googleapis.com/css2?family=Crimson+Text:wght@400;600&display=swap" rel="stylesheet">
<style>
  :root{
    --page:#e9e7e3;
    --steel-dark:#6e7176;
    --steel-mid:#a4a7ab;
    --steel-light:#e6e7e9;
    --ink:#2b2d31;
    --gold:#e5b80b;
    --navy:#1f2f86;
    --rule:#3a3c40;
    --eagle-tone:#c9cacd;
  }
  *{box-sizing:border-box;margin:0;padding:0}
  html,body{width:1200px;height:900px;overflow:hidden;background:var(--page)}
  body{font-family:"Crimson Text",Georgia,serif;color:var(--ink)}
  .sheet{position:relative;width:1200px;height:900px}
  .card{
    position:absolute;left:270px;width:660px;height:377px;border-radius:28px;overflow:hidden;
    background:linear-gradient(100deg,var(--steel-mid) 0%,var(--steel-dark) 22%,var(--steel-mid) 38%,var(--steel-dark) 52%,var(--steel-light) 70%,var(--steel-mid) 84%,var(--steel-light) 100%);
    box-shadow:0 10px 28px rgba(0,0,0,.25);
  }
  .card--front{top:48px}
  .card--back{top:475px}
  .eagle-mark{position:absolute;right:40px;top:18px;width:300px;height:240px;border-radius:50% 45% 40% 55%;
    background:radial-gradient(ellipse at 40% 40%,rgba(201,202,205,.55),rgba(201,202,205,0) 70%)}
  .brand{position:absolute;display:flex;align-items:center;gap:10px;font-weight:600;font-size:22px;color:var(--navy);line-height:1.05}
  .brand__dot{width:34px;height:34px;border-radius:50%;background:var(--navy);flex:none}
  .card--front .brand{left:40px;top:258px;width:200px}
  .card--back .brand{left:40px;top:270px;width:210px}
  .divider{position:absolute;width:1px;background:var(--rule)}
  .card--front .divider{left:250px;top:185px;height:160px}
  .card--back .divider{left:265px;top:205px;height:150px}
  .services{position:absolute;left:275px;top:190px}
  .services__title{font-size:24px;color:var(--gold);letter-spacing:.5px;margin-bottom:4px}
  .services__list{list-style:none;font-size:19px;line-height:1.35}
  .services__list li{display:flex;align-items:center;gap:10px}
  .services__list li::before{content:"";width:10px;height:10px;border-radius:50%;background:var(--navy);box-shadow:0 0 0 2px rgba(31,47,134,.3)}
  .person{position:absolute;left:40px;top:38px}
  .person__name{font-size:28px;color:var(--gold);letter-spacing:.5px;line-height:1}
  .person__role{font-size:20px;margin-bottom:4px}
  .contact{list-style:none;font-size:19px;line-height:1.4}
  .contact li{display:flex;align-items:center;gap:10px}
  .contact svg{width:16px;height:16px;flex:none;fill:var(--navy)}
  .office{position:absolute;left:285px;top:208px}
</style>
</head>
<body>
<main class="sheet">
  <section class="card card--front">
    <div class="eagle-mark" role="img" aria-label="Faint large eagle head decoration"></div>
    <div class="brand"><span class="brand__dot"></span>Harbinger Slabworks, Inc.</div>
    <div class="divider"></div>
    <div class="services">
      <h2 class="services__title">OUR SERVICES</h2>
      <ul class="services__list">
        <li>Wall Sawing</li>
        <li>Core Drilling</li>
        <li>Slab Sawing</li>
        <li>Breaking &amp; Removal</li>
      </ul>
    </div>
  </section>

  <section class="card card--back">
    <div class="eagle-mark" role="img" aria-label="Faint large eagle head decoration"></div>
    <div class="person">
      <h1 class="person__name">MAREN DELGADO</h1>
      <p class="person__role">Operations and Finance</p>
      <ul class="contact">
        <li><svg viewBox="0 0 16 16"><path d="M5 1h6a1 1 0 0 1 1 1v12a1 1 0 0 1-1 1H5a1 1 0 0 1-1-1V2a1 1 0 0 1 1-1zm.5 2v9h5V3z"/></svg>555.014.2280</li>
        <li><svg viewBox="0 0 16 16"><path d="M1 3h14v10H1zm1.5 1.5v.4L8 9l5.5-4.1v-.4z"/></svg>maren@harbingerslabworks.com</li>
      </ul>
    </div>
    <div class="brand"><span class="brand__dot"></span>Harbinger Slabworks, Inc.</div>
    <div class="divider"></div>
    <ul class="contact office">
      <li><svg viewBox="0 0 16 16"><path d="M3.5 1.5l2.5 3-1.5 1.5a9 9 0 0 0 5.5 5.5L11.5 10l3 2.5-1.5 2.5C7 15 1 9 1 3z"/></svg>555.018.4470</li>
      <li><svg viewBox="0 0 16 16"><path d="M3.5 1.5l2.5 3-1.5 1.5a9 9 0 0 0 5.5 5.5L11.5 10l3 2.5-1.5 2.5C7 15 1 9 1 3z"/></svg>555-Slabcut</li>
      <li><svg viewBox="0 0 16 16"><path d="M8 1a7 7 0 1 0 0 14A7 7 0 0 0 8 1zm0 1.5c.8 0 1.7 1.9 1.9 4.5H6.1C6.3 4.4 7.2 2.5 8 2.5zM2.6 7h2a12 12 0 0 1 .6-3.6A5.5 5.5 0 0 0 2.6 7zm0 2a5.5 5.5 0 0 0 2.6 3.6A12 12 0 0 1 4.6 9zm3.5 0h3.8c-.2 2.6-1.1 4.5-1.9 4.5S6.3 11.6 6.1 9zm5.3 0a12 12 0 0 1-.6 3.6A5.5 5.5 0 0 0 13.4 9zm0-2h2a5.5 5.5 0 0 0-2.6-3.6c.3 1 .5 2.2.6 3.6z"/></svg>www.harbingerslabworks.com</li>
      <li><svg viewBox="0 0 16 16"><path d="M8 1a5 5 0 0 1 5 5c0 3.5-5 9-5 9S3 9.5 3 6a5 5 0 0 1 5-5zm0 3a2 2 0 1 0 0 4 2 2 0 0 0 0-4z"/></svg>48 North Alder Lane, Ridgefield, NJ 07000</li>
    </ul>
  </section>
</main>
</body>
</html>
```